Heating and Air Conditioning Company Van

This will be the first van in my fleet that I am getting wrapped. Looking to utilize the colors in the motorcycle pic and possibly add some hints of red for heating (or maybe not). I am looking for a full wrap design.

My company does heating and air conditioning with a focus on energy efficient systems. I want to convey the energy efficiency with the green and blue but also want it to look like an HVAC truck (usually red and blue), but also want to stand out from the rest of the HVAC companies.

Ive also attached a picture of a van wrap that somebody else did for me that I kind of like but don't love.

```html
<!DOCTYPE html>
<html lang="en">
<head>
<meta charset="utf-8">
<title>Greenleaf Heating &amp; Air Conditioning – Van Wrap</title>
<link href="https://fonts.googleapis.com/css2?family=Exo+2:ital,wght@0,700;0,800;1,700;1,800&family=Open+Sans:wght@400&display=swap" rel="stylesheet">
<style>
  :root {
    --wrap-white: #ffffff;
    --brand-blue: #0d4f94;
    --lime-light: #d2f53e;
    --lime: #a6e21f;
    --lime-deep: #82c816;
    --phone-green: #8cd31e;
    --page-bg: #d9d9d9;
  }
  * { margin: 0; padding: 0; box-sizing: border-box; }
  html, body {
    width: 1200px; height: 641px; overflow: hidden;
    background: var(--page-bg);
  }
  .wrap-panel {
    position: relative;
    width: 1200px; height: 641px;
    overflow: hidden;
    background: var(--wrap-white);
  }
  .wrap-shapes { position: absolute; inset: 0; }
  .contact-phone {
    position: absolute; left: 176px; top: 328px;
    display: flex; align-items: center; gap: 8px;
    font-family: "Exo 2", sans-serif; font-weight: 800; font-style: italic;
    font-size: 30px; color: var(--brand-blue); letter-spacing: 0.5px;
  }
  .contact-phone svg { width: 24px; height: 24px; }
  .tagline {
    position: absolute; left: 640px; top: 170px;
    font-family: "Exo 2", sans-serif; font-weight: 700; font-style: italic;
    font-size: 27px; line-height: 1.05; color: var(--brand-blue);
    text-transform: uppercase;
  }
  .brand-mark {
    position: absolute; left: 930px; top: 100px;
    width: 104px; height: 104px;
    background: var(--wrap-white);
  }
  .brand-name {
    position: absolute; left: 636px; top: 236px;
    font-family: "Exo 2", sans-serif; font-weight: 800;
    font-size: 78px; line-height: 1; color: var(--brand-blue);
  }
  .brand-service {
    position: absolute; left: 620px; top: 318px;
    font-family: "Open Sans", sans-serif; font-weight: 400;
    font-size: 28px; color: var(--brand-blue); letter-spacing: 0.5px;
    white-space: nowrap;
  }
  .web-pill {
    position: absolute; left: 560px; top: 388px;
    width: 316px; height: 34px; border-radius: 8px;
    background: var(--brand-blue);
    display: flex; align-items: center; justify-content: center;
    font-family: "Exo 2", sans-serif; font-weight: 700; font-style: italic;
    font-size: 17px; color: var(--wrap-white);
  }
</style>
</head>
<body>
  <main class="wrap-panel">
    <svg class="wrap-shapes" viewBox="0 0 1200 641" width="1200" height="641">
      <defs>
        <radialGradient id="lime-glow" cx="0.72" cy="0.42" r="0.75">
          <stop offset="0" stop-color="var(--lime-light)"/>
          <stop offset="0.55" stop-color="var(--lime)"/>
          <stop offset="1" stop-color="var(--lime-deep)"/>
        </radialGradient>
      </defs>
      <rect class="sunburst-field" x="0" y="0" width="1200" height="641" fill="url(#lime-glow)"
            role="img" aria-label="Lime green sunburst rays radiating from behind the company name"/>
      <path class="white-front" d="M0,0 H548 C535,250 468,430 340,641 H0 Z" fill="var(--wrap-white)"/>
      <path class="blue-swoosh" d="M548,0 H592 C580,255 515,450 398,641 H340 C468,430 535,250 548,0 Z" fill="var(--brand-blue)"/>
    </svg>

    <div class="contact-phone">
      <svg viewBox="0 0 24 24" aria-hidden="true">
        <path d="M6.6 10.8c1.4 2.8 3.8 5.1 6.6 6.6l2.2-2.2c.3-.3.7-.4 1-.2 1.1.4 2.3.6 3.6.6.6 0 1 .4 1 1V20c0 .6-.4 1-1 1C10.6 21 3 13.4 3 4c0-.6.4-1 1-1h3.5c.6 0 1 .4 1 1 0 1.3.2 2.5.6 3.6.1.3 0 .7-.2 1l-2.3 2.2z" fill="var(--phone-green)"/>
      </svg>
      <span>555-201-4873</span>
    </div>

    <p class="tagline">Your trusted<br>HVAC installers</p>
    <div class="brand-mark" role="img" aria-label="Company mark"></div>
    <h1 class="brand-name">Greenleaf</h1>
    <p class="brand-service">HEATING &amp; AIR CONDITIONING</p>
    <p class="web-pill">greenleafheatingandac.com</p>
  </main>
</body>
</html>
```